Varnock Travel letterhead design

We need a design for a simple document where we can dump our own information within it. A simple letterhead style. No address or phone details etc are required. More just our logo and free format. Hope this makes sense !

```html
<!DOCTYPE html>
<html lang="en">
<head>
<meta charset="utf-8">
<title>Varnock Travel Letterhead</title>
<link href="https://fonts.googleapis.com/css2?family=Montserrat:wght@800&family=Roboto:wght@400;700&display=swap" rel="stylesheet">
<style>
  :root {
    --backdrop: #7f8590;
    --paper: #ffffff;
    --navy: #22457a;
    --gold: #b5a22b;
    --body-grey: #9a9a9a;
    --footer-dark: #2c3340;
    --band-grey: #b9babe;
  }
  html, body {
    margin: 0;
    width: 1200px;
    height: 1200px;
    overflow: hidden;
    background: var(--backdrop);
  }
  .letterhead {
    position: absolute;
    left: 201px;
    top: 60px;
    width: 798px;
    height: 1080px;
    background: var(--paper);
    font-family: "Roboto", Arial, sans-serif;
  }
  .brand-name {
    position: absolute;
    left: 145px;
    top: 108px;
    margin: 0;
    font-family: "Montserrat", Arial, sans-serif;
    font-weight: 800;
    font-size: 40px;
    letter-spacing: -0.5px;
    color: var(--navy);
    line-height: 1;
  }
  .letter-body {
    position: absolute;
    left: 145px;
    top: 288px;
    width: 527px;
  }
  .section-heading {
    margin: 0 0 14px;
    font-size: 13px;
    font-weight: 700;
    letter-spacing: 1.5px;
    text-transform: uppercase;
    color: var(--gold);
  }
  .section-heading.second {
    margin-top: 40px;
  }
  .letter-body p {
    margin: 0 0 14px;
    font-size: 11px;
    line-height: 16px;
    color: var(--body-grey);
  }
  .signature-area {
    position: absolute;
    left: 545px;
    top: 722px;
    width: 108px;
    height: 56px;
    background: linear-gradient(135deg, #f2f2f3, #e3e4e6);
  }
  .letter-footer {
    position: absolute;
    left: 145px;
    top: 972px;
    margin: 0;
    font-size: 10px;
    letter-spacing: 1px;
    color: var(--footer-dark);
  }
  .bottom-band {
    position: absolute;
    left: 0;
    bottom: 0;
    width: 798px;
    height: 34px;
    display: block;
  }
</style>
</head>
<body>
  <main class="letterhead">
    <h1 class="brand-name">Varnock Travel</h1>

    <section class="letter-body">
      <h2 class="section-heading">Welcome to our journey</h2>
      <p>Thank you for choosing us to plan your next trip. Our team arranges flights, hotels and tours with care, so every part of your travel runs smoothly from the first booking to the final return home.</p>
      <p>We look forward to hearing from you and shaping a route that suits you.</p>

      <h2 class="section-heading second">Details of your booking</h2>
      <p>Please review the itinerary below and let us know of any changes. All times shown are local, and each transfer has been confirmed with our partners in advance of your arrival.</p>
      <p>Should your plans shift, we will rebook quickly and keep costs low. Travel documents will follow by post in the coming days.</p>
      <p>With kind regards from the whole team.</p>
    </section>

    <div class="signature-area" role="img" aria-label="Handwritten signature"></div>

    <p class="letter-footer">Reference 0042 · Page 1 of 1</p>

    <svg class="bottom-band" viewBox="0 0 798 34" aria-hidden="true">
      <polygon points="0,0 395,0 366,34 0,34" fill="var(--band-grey)"/>
      <polygon points="414,0 798,0 798,34 385,34" fill="var(--navy)"/>
    </svg>
  </main>
</body>
</html>
```